Real Estate Team Needs Business Cards

Double sided - Team Member on Front, Team Leader on Back (back side will contain more details).
Colors to use:
Red = R: 233 G: 1 B: 2
Grey = R: 89 G: 89 B: 89
Black= R: 0 B: 0 B: 0
** MAIN FOCUS ** ( separate border, color, design, etc. to really stand out - whatever you think draws the most attention ) on both sides for "Sell for 1%‡" and "Buy & receive up to a 1% rebate‡". Must have fine print **
**Please make both sides stand out and look unique / different
Business card to have round corners (standard size 3.5" x 2").:
Document Trim Size
89 x 51 mm
1050 x 600 pixels
Full Bleed Size
92 x 54 mm
1085 x 635 pixels
Basic example provided. Please redesign as you see best. In your design - Please use the same picture on both sides. Name, address, phone number, email, etc. will be provided to the selected design. QR code on back side only if there is room (not important)

```html
<!DOCTYPE html>
<html lang="en">
<head>
<meta charset="utf-8">
<title>Summit Lane Realty – Business Cards</title>
<link href="https://fonts.googleapis.com/css2?family=PT+Sans:ital,wght@0,400;0,700;1,400;1,700&display=swap" rel="stylesheet">
<style>
  :root {
    --red: #e90102;
    --grey: #595959;
    --black: #000000;
    --card: #f4f4f4;
    --white: #ffffff;
    --backdrop: #e6e3de;
    --photo-top: #c9ccd3;
    --photo-bottom: #26407a;
  }
  * { margin: 0; padding: 0; box-sizing: border-box; }
  html, body {
    width: 900px; height: 1200px; overflow: hidden;
    background: var(--backdrop);
    font-family: "PT Sans", Arial, sans-serif;
  }
  .card {
    position: absolute; left: 75px; width: 768px;
    background: var(--card); border-radius: 14px; overflow: hidden;
    box-shadow: 0 4px 14px rgba(0,0,0,0.25);
  }
  .card--member { top: 133px; height: 438px; }
  .card--leader { top: 627px; height: 441px; }

  .portrait {
    position: absolute;
    background: linear-gradient(180deg, var(--photo-top) 0%, #b7bcc6 45%, var(--photo-bottom) 80%);
  }
  .card--member .portrait { left: 0; top: 35px; width: 300px; height: 305px; }
  .card--leader .portrait { left: 25px; top: 28px; width: 300px; height: 305px; }

  .bands { position: absolute; left: 0; top: 0; width: 768px; height: 100%; }

  .brand {
    position: absolute; text-align: center; width: 430px;
  }
  .card--member .brand { left: 310px; top: 112px; }
  .card--leader .brand { left: 330px; top: 118px; }
  .brand__name {
    display: inline-flex; align-items: center; gap: 10px;
    font-weight: 700; font-size: 34px; color: var(--black);
    letter-spacing: 0.5px; line-height: 1;
  }
  .brand__mark { width: 18px; height: 18px; background: var(--red); display: inline-block; }
  .brand__sub {
    display: flex; align-items: center; gap: 8px; margin: 6px auto 0; width: 405px;
    font-size: 9px; font-weight: 700; color: var(--grey); letter-spacing: 0.5px;
  }
  .brand__sub::before, .brand__sub::after {
    content: ""; flex: 1; height: 2px; background: var(--red);
  }

  .offer {
    position: absolute; text-align: center; width: 470px;
    color: var(--red); font-style: italic; font-size: 23px; line-height: 27px;
  }
  .card--member .offer { left: 290px; top: 200px; }
  .card--leader .offer { left: 315px; top: 212px; }

  .services {
    position: absolute; left: 290px; top: 272px; width: 470px;
    list-style: none; text-align: center;
    font-size: 21px; line-height: 27.5px; color: var(--black);
  }

  .web {
    position: absolute; font-weight: 700; letter-spacing: 0.6px; font-size: 19px;
  }
  .card--member .web { left: 355px; top: 377px; width: 400px; text-align: center; color: var(--white); }
  .card--leader .web { left: 330px; top: 295px; width: 440px; text-align: center; color: var(--black); }

  .person { position: absolute; color: var(--white); }
  .person__name { font-weight: 700; font-size: 23px; letter-spacing: 2px; line-height: 1; }
  .person__role { font-weight: 700; font-size: 18px; letter-spacing: 1px; margin-top: 7px; }
  .card--member .person { left: 30px; top: 366px; width: 270px; text-align: center; }
  .card--leader .person { left: 38px; top: 358px; text-align: left; }
  .card--leader .person__role { font-size: 17px; letter-spacing: 0.3px; }

  .contact {
    position: absolute; left: 355px; top: 358px; width: 400px;
    text-align: center; color: var(--white); font-weight: 700; font-size: 18px; line-height: 31px;
    letter-spacing: 0.3px;
  }
</style>
</head>
<body>

<section class="card card--member">
  <div class="portrait" role="img" aria-label="Portrait photo of the team member in a navy suit and light blue tie"></div>
  <svg class="bands" viewBox="0 0 768 438" aria-hidden="true">
    <polygon points="325,370 768,370 768,412 355,412" fill="var(--black)"/>
    <polygon points="0,340 300,340 370,438 0,438" fill="var(--red)"/>
  </svg>
  <div class="brand">
    <div class="brand__name"><span class="brand__mark"></span>SUMMIT LANE REALTY</div>
    <div class="brand__sub">INC., BROKERAGE</div>
  </div>
  <p class="offer">Sell for 1%*<br>Buy &amp; Receive up to a 1% rebate*</p>
  <ul class="services">
    <li>Free Home Evaluation</li>
    <li>Advanced Property Search</li>
    <li>Free Local Sold Reports</li>
  </ul>
  <div class="web">WWW.SUMMITLANEREALTY.COM</div>
  <div class="person">
    <div class="person__name">JOHNATHAN DOE</div>
    <div class="person__role">OWNER</div>
  </div>
</section>

<section class="card card--leader">
  <div class="portrait" role="img" aria-label="Portrait photo of the team leader in a navy suit and light blue tie"></div>
  <svg class="bands" viewBox="0 0 768 441" aria-hidden="true">
    <polygon points="0,333 365,333 320,441 0,441" fill="var(--black)"/>
    <polygon points="369,333 768,333 768,441 324,441" fill="var(--red)"/>
  </svg>
  <div class="brand">
    <div class="brand__name"><span class="brand__mark"></span>SUMMIT LANE REALTY</div>
    <div class="brand__sub">INC., BROKERAGE</div>
  </div>
  <p class="offer">Sell for 1%*<br>Buy &amp; Receive up to a 1% rebate*</p>
  <div class="web">WWW.SUMMITLANEREALTY.COM</div>
  <div class="person">
    <div class="person__name">JOHNATHAN DOE</div>
    <div class="person__role">POSITION</div>
  </div>
  <div class="contact">
    PH: 123 456 7890 | M: 123 456 789<br>
    CONTACT@SUMMITLANEREALTY.COM
  </div>
</section>

</body>
</html>
```